LinkedIn Ad Image Design Competition

We're seeking creative designers to develop a series of engaging LinkedIn advertisements for Tidelark with original art work.

The goal is to create scroll-stopping ads that capture attention through humor, nostalgia, and compelling storytelling while maintaining professional appeal.

Creative Brief:
Please read the "Core Messages to Convey"
https://notes.quillharbor.net/page/d/7kwtrVbQ3MeHxnLsYpRCuA52-h08tjzNG_e61mqaLp4/view?tab=t.0#section=h.4rkdwmqhz2c

Target Market(s)

Busy executives focusing on making their company more efficient

Requirements
Must have
• An image ( not copy) that speaks to one of our "Core Messages to Convey"

```html
<!DOCTYPE html>
<html lang="en">
<head>
<meta charset="utf-8">
<title>Tidelark – Accelerate your value creation journey</title>
<link rel="stylesheet" href="https://fonts.googleapis.com/css2?family=Poppins:wght@600;700;800&family=Oswald:wght@600&family=Mrs+Saint+Delafield&display=swap">
<style>
  :root {
    --ink: #16141f;
    --red: #d42a2a;
    --deep-red: #6e0707;
    --tan: #b8823f;
    --gold: #ffe500;
    --slate: #4a4d52;
    --white: #ffffff;
    --paper: #f4f4f6;
    --sand-light: #ead2ad;
    --sand-dark: #c9a172;
  }
  * { margin: 0; padding: 0; box-sizing: border-box; }
  html, body { width: 1200px; height: 1200px; overflow: hidden; background: var(--white); }
  .ad {
    position: relative; width: 1200px; height: 1200px; overflow: hidden;
    background: linear-gradient(160deg, var(--white) 30%, var(--paper) 70%, #e6e7ea 100%);
    font-family: "Poppins", sans-serif; color: var(--ink);
  }
  .data-backdrop {
    position: absolute; left: 0; top: 300px; width: 820px; height: 480px;
    background: radial-gradient(ellipse at 60% 40%, rgba(200,200,206,0.45), rgba(255,255,255,0) 70%);
  }
  .sand-scene {
    position: absolute; left: 0; top: 760px; width: 1200px; height: 440px;
    background: linear-gradient(180deg, var(--sand-light) 0%, #dfbf92 45%, var(--sand-dark) 100%);
    border-top-left-radius: 60% 40px; border-top-right-radius: 40% 30px;
  }
  .clock-scene {
    position: absolute; left: 640px; top: 240px; width: 460px; height: 500px;
    border-radius: 50%;
    background: radial-gradient(circle at 55% 50%, #f7f7f8 0%, #dcdde0 55%, #b9babe 75%, rgba(230,230,233,0) 78%);
  }
  .brand {
    position: absolute; right: 108px; top: 92px;
    font-weight: 700; font-size: 60px; line-height: 1; letter-spacing: -1px; color: var(--ink);
  }
  .headline { position: absolute; left: 72px; top: 84px; font-weight: 700; line-height: 1; }
  .headline .lead { display: block; font-size: 58px; letter-spacing: -0.5px; }
  .headline .your { display: block; font-size: 104px; margin: -14px 0 0 184px; letter-spacing: -2px; }
  .headline .accent { display: block; color: var(--red); font-size: 84px; line-height: 83px; letter-spacing: -1.5px; margin-top: -6px; }
  .choice {
    position: absolute; color: var(--white); font-weight: 700; font-size: 41px; line-height: 47px;
    border-radius: 24px; display: flex; align-items: center;
  }
  .choice-stress { left: 80px; top: 526px; width: 650px; height: 178px; background: var(--ink); padding-left: 48px; }
  .choice-beach {
    left: 430px; top: 710px; width: 682px; height: 180px; padding-left: 260px;
    background: linear-gradient(90deg, #8a0b0b, var(--deep-red));
  }
  .growth-arrow { position: absolute; left: 0; top: 0; width: 1200px; height: 1200px; pointer-events: none; }
  .or-badge {
    position: absolute; left: 554px; top: 646px; width: 102px; height: 102px; border-radius: 50%;
    background: var(--red); border: 5px solid var(--white); color: var(--white);
    font-weight: 700; font-size: 42px; display: flex; align-items: center; justify-content: center; padding-bottom: 4px;
  }
  .tagline { position: absolute; left: 68px; top: 848px; }
  .tagline .script { font-family: "Mrs Saint Delafield", cursive; font-size: 66px; line-height: 52px; display: block; }
  .tagline .script.second { margin-left: 40px; }
  .tagline .bold { display: block; font-weight: 700; font-size: 40px; line-height: 45px; margin-top: 6px; }
  .prize-label {
    position: absolute; left: 424px; top: 992px; width: 200px; height: 100px; background: var(--tan);
    border-radius: 14px; color: var(--white); font-weight: 700; font-size: 34px; line-height: 36px;
    padding: 14px 0 0 28px;
  }
  .prize { position: absolute; top: 959px; width: 166px; height: 166px; }
  .prize svg { position: absolute; inset: 0; }
  .prize .place, .prize .amount { position: absolute; left: 0; width: 100%; text-align: center; }
  .prize .place { top: 38px; color: var(--white); font-weight: 700; font-size: 26px; }
  .prize .amount { top: 68px; color: var(--gold); font-family: "Oswald", sans-serif; font-weight: 600; font-size: 42px; line-height: 1; }
  .prize-first { left: 584px; }
  .prize-second { left: 764px; }
  .prize-third { left: 942px; }
</style>
</head>
<body>
<main class="ad">
  <div class="data-backdrop" role="img" aria-label="Faint columns of binary digits fading across the background"></div>
  <div class="clock-scene" role="img" aria-label="A white wall clock shattering into glass shards and brass gears"></div>
  <div class="sand-scene" role="img" aria-label="Soft rolling beach sand dunes"></div>

  <div class="brand">Tidelark</div>

  <h1 class="headline">
    <span class="lead">Accelerate</span>
    <span class="your">your</span>
    <span class="accent">value</span>
    <span class="accent">creation</span>
    <span class="accent">journey</span>
  </h1>

  <div class="choice choice-stress">STRESS OVER<br>DISPARATE DATA</div>
  <div class="choice choice-beach">SPEND TIME AT<br>THE BEACH</div>

  <svg class="growth-arrow" viewBox="0 0 1200 1200" aria-hidden="true">
    <polyline points="313,995 495,752 540,790 610,700 655,725 730,612 762,640 790,505"
      fill="none" stroke="#c41414" stroke-width="26" stroke-linejoin="miter" stroke-linecap="butt"/>
    <polygon points="756,512 808,440 826,530" fill="#c41414"/>
  </svg>

  <div class="or-badge">or</div>

  <div class="tagline">
    <span class="script">Turn</span>
    <span class="script second">disparate</span>
    <span class="bold">DATA INTO<br>UNIFIED<br>INSIGHTS</span>
  </div>

  <div class="prize-label">PRIZE<br>POOL</div>

  <div class="prize prize-first">
    <svg viewBox="0 0 166 166" aria-hidden="true">
      <circle cx="83" cy="83" r="74" fill="#b51616"/>
      <circle cx="83" cy="83" r="74" fill="none" stroke="#b51616" stroke-width="14" stroke-linecap="round" stroke-dasharray="0 19.37"/>
    </svg>
    <div class="place">1ST</div><div class="amount">$1,000</div>
  </div>
  <div class="prize prize-second">
    <svg viewBox="0 0 166 166" aria-hidden="true">
      <circle cx="83" cy="83" r="74" fill="#1c1b24"/>
      <circle cx="83" cy="83" r="74" fill="none" stroke="#1c1b24" stroke-width="14" stroke-linecap="round" stroke-dasharray="0 19.37"/>
    </svg>
    <div class="place">2ND</div><div class="amount">$750</div>
  </div>
  <div class="prize prize-third">
    <svg viewBox="0 0 166 166" aria-hidden="true">
      <circle cx="83" cy="83" r="74" fill="#4a4d52"/>
      <circle cx="83" cy="83" r="74" fill="none" stroke="#4a4d52" stroke-width="14" stroke-linecap="round" stroke-dasharray="0 19.37"/>
    </svg>
    <div class="place">3RD</div><div class="amount">$500</div>
  </div>
</main>
</body>
</html>
```